Have Logo - Need Business Card Design!!!

I am looking for a business card design for a real estate development business. The company name is Quillhaven Property Partners. I already have a logo created by Sketch Harbor and would like this logo to be incorporated into the design. I have uploaded the files. The card needs to be professional, but visually interesting. Not necessary to be double-sided, but if you want to get creative and can think of something to put on the back then have at it.

Target Market(s)

The target audience for these business cards will be professionals in the real estate industry.

Industry/Entity Type

Real Estate

Requirements
Must have
• The business card must have all the necessary items for a business card, i.e. company name, our logo, name (however, not title necessary), office address, office phone number, cell number, fax number, website address, etc.

You can use the information below for the card:

Gregory L. Hanlon
782 Marlowe Avenue
San Francisco, California 94127

www.quillhavenpartners.example
ghanlon@quillhavenpartners.example
Office: 415-555-0142
Fax: 415-555-0143
Cell: 415-555-0186

```html
<!DOCTYPE html>
<html lang="en">
<head>
<meta charset="utf-8">
<title>Quillhaven Property Partners — Business Card</title>
<link rel="stylesheet" href="https://fonts.googleapis.com/css2?family=Arimo:wght@400;700&display=swap">
<style>
  :root {
    --green: #1d8a3c;
    --navy: #25336b;
    --ink: #2b2b2b;
    --card: #ffffff;
    --backdrop: #e6e6e6;
  }
  * { margin: 0; padding: 0; box-sizing: border-box; }
  html, body { width: 1200px; height: 951px; overflow: hidden; }
  body {
    background: var(--backdrop);
    font-family: "Arimo", Arial, sans-serif;
    color: var(--ink);
    position: relative;
  }
  .card {
    position: absolute;
    width: 640px;
    height: 366px;
    background: var(--card);
    border-radius: 18px;
    overflow: hidden;
    box-shadow: 0 6px 18px rgba(0,0,0,0.18);
  }
  .card--front { left: 110px; top: 80px; }
  .card--back  { left: 450px; top: 505px; }

  .brand__name { color: var(--ink); font-weight: 400; white-space: nowrap; }

  .card--front .brand__name {
    position: absolute; left: 0; right: 0; top: 126px;
    text-align: center; font-size: 38px;
  }
  .card--front .website {
    position: absolute; left: 0; right: 0; top: 258px;
    text-align: center; font-size: 19px; font-weight: 700; color: var(--ink);
  }

  .card--back .brand__name { position: absolute; left: 26px; top: 40px; font-size: 22px; }

  .panel { position: absolute; inset: 0; width: 640px; height: 366px; }

  .contact { position: absolute; left: 26px; top: 128px; list-style: none; font-size: 15px; line-height: 1.2; }
  .contact li { display: flex; align-items: flex-start; gap: 8px; margin-bottom: 3px; }
  .contact li.contact__address { margin-bottom: 10px; }
  .contact svg { width: 14px; height: 14px; flex: none; margin-top: 1px; fill: var(--green); }

  .holder {
    position: absolute; left: 420px; right: 20px; top: 170px;
    text-align: center; color: #fff; font-size: 22px; font-weight: 400;
  }
</style>
</head>
<body>

<section class="card card--front" aria-label="Business card front">
  <p class="brand__name">Quillhaven Property Partners</p>
  <p class="website">www.quillhavenpartners.example</p>
</section>

<section class="card card--back" aria-label="Business card back">
  <svg class="panel" viewBox="0 0 640 366" aria-hidden="true">
    <path d="M 350 0 C 395 110, 405 250, 360 366 L 400 366 C 430 250, 415 110, 362 0 Z" fill="var(--navy)"/>
    <path d="M 362 0 C 415 110, 430 250, 396 366 L 640 366 L 640 0 Z" fill="var(--green)"/>
  </svg>

  <p class="brand__name">Quillhaven Property Partners</p>

  <ul class="contact">
    <li class="contact__address">
      <svg viewBox="0 0 16 16"><path d="M8 1 L1 7.5 H3 V15 H6.5 V10.5 H9.5 V15 H13 V7.5 H15 Z"/></svg>
      <span>782 Marlowe Avenue<br>San Francisco, California 94127</span>
    </li>
    <li>
      <svg viewBox="0 0 16 16"><path d="M3.5 1.5 L6 1 L7.5 5 L5.8 6.3 C6.6 8 8 9.4 9.7 10.2 L11 8.5 L15 10 L14.5 12.5 C14.2 14 12.5 15 11 14.6 C6.5 13.4 2.6 9.5 1.4 5 C1 3.5 2 1.8 3.5 1.5 Z"/></svg>
      <span>415-555-0142</span>
    </li>
    <li>
      <svg viewBox="0 0 16 16"><path d="M4 1 H11 V5 H4 Z M2 6 H14 V12 H12 V15 H4 V12 H2 Z M5 10 V13.5 H11 V10 Z"/></svg>
      <span>415-555-0143</span>
    </li>
    <li>
      <svg viewBox="0 0 16 16"><path d="M5 0.5 H11 A1.5 1.5 0 0 1 12.5 2 V14 A1.5 1.5 0 0 1 11 15.5 H5 A1.5 1.5 0 0 1 3.5 14 V2 A1.5 1.5 0 0 1 5 0.5 Z M5 2.5 V12 H11 V2.5 Z"/></svg>
      <span>415-555-0186</span>
    </li>
    <li>
      <svg viewBox="0 0 16 16"><path d="M1 3.5 H15 V13 H1 Z M1.5 4 L8 9 L14.5 4 V5.2 L8 10.3 L1.5 5.2 Z" fill-rule="evenodd"/></svg>
      <span>ghanlon@quillhavenpartners.example</span>
    </li>
    <li>
      <svg viewBox="0 0 16 16"><circle cx="8" cy="8" r="7"/></svg>
      <span>www.quillhavenpartners.example</span>
    </li>
  </ul>

  <p class="holder">Gregory L. Hanlon</p>
</section>

</body>
</html>
```